Quorbanil Business Cards & Stationery Design
Business Cards & Stationery Design
Quorbanil Business Cards & Stationery Design - Information Technology
Creative Brief
Professional
Neville Prothick
Technical Consultant
47 marbury close fenwick NSW 2012 Australia
nprothick@quorbanil.example
http://www.quorbanil.example
The font used is called Aller, and can be downloaded from : http://www.glyphmerrow.example/buyonline/fonts/aller
www.quorbanil.example

```html
<!DOCTYPE html>
<html lang="en">
<head>
<meta charset="utf-8">
<title>Quorbanil Business Cards &amp; Stationery</title>
<link rel="stylesheet" href="https://fonts.googleapis.com/css2?family=Ubuntu:wght@400;500&display=swap">
<style>
  :root {
    --bg: #e9e7e3;
    --paper: #ffffff;
    --ink: #3a3a3a;
    --ink-soft: #7a7a7a;
    --green: #1f9a2e;
    --green-dark: #0f6b1c;
    --bar-dark: #1d1d1d;
    --bar-mid: #8a8a8a;
    --faint: #f1f3f1;
    --shadow: 0 2px 8px rgba(0,0,0,.18);
  }
  * { box-sizing: border-box; margin: 0; padding: 0; }
  html, body { width: 1200px; height: 840px; overflow: hidden; }
  body {
    position: relative;
    background: var(--bg);
    font-family: "Ubuntu", sans-serif;
    color: var(--ink);
  }
  .sheet {
    position: absolute;
    background: var(--paper);
    box-shadow: var(--shadow);
    overflow: hidden;
  }
  .brand { display: flex; align-items: center; gap: 6px; }
  .brand-mark { background: var(--green); display: block; }
  .brand-name { font-weight: 500; color: var(--ink); letter-spacing: -0.5px; line-height: 1; }
  .contact { font-size: 6px; line-height: 1.5; color: var(--ink-soft); }
  .footer-bar {
    position: absolute; left: 0; right: 0; bottom: 0;
    display: flex; align-items: stretch;
  }
  .footer-bar .rule { flex: 1; background: linear-gradient(90deg, var(--bar-mid), var(--bar-dark)); }
  .footer-bar .url {
    background: var(--green); color: #fff; font-size: 6px;
    display: flex; align-items: center; padding: 0 10px;
  }

  /* Letterhead */
  .letterhead { left: 80px; top: 120px; width: 390px; height: 552px; }
  .letterhead .brand { position: absolute; left: 30px; top: 30px; }
  .letterhead .brand-mark { width: 14px; height: 14px; }
  .letterhead .brand-name { font-size: 22px; }
  .letterhead .contact { position: absolute; left: 250px; top: 28px; }
  .letterhead .contact .web { margin-top: 4px; color: var(--ink); }
  .letterhead .watermark {
    position: absolute; left: 110px; top: 230px; width: 170px; height: 170px;
    background: var(--faint);
  }
  .letterhead .footer-bar { height: 7px; bottom: 14px; }

  /* Envelope front */
  .envelope { left: 520px; top: 100px; width: 400px; height: 200px; }
  .envelope .brand { position: absolute; left: 22px; top: 24px; }
  .envelope .brand-mark { width: 10px; height: 10px; }
  .envelope .brand-name { font-size: 17px; }
  .envelope .contact { position: absolute; left: 22px; top: 52px; }
  .envelope .footer-bar { height: 6px; bottom: 12px; }

  /* Envelope back */
  .envelope-back { left: 945px; top: 100px; width: 190px; height: 200px; background: #f6f6f6; }
  .envelope-back svg { position: absolute; inset: 0; }
  .envelope-back .brand-mark { position: absolute; left: 89px; top: 30px; width: 12px; height: 12px; }

  /* Business card front */
  .card { width: 280px; height: 182px; border-radius: 8px; }
  .card-front { left: 520px; top: 350px; }
  .card-front .identity {
    position: absolute; left: 0; top: 0; bottom: 0; width: 150px;
    display: flex; flex-direction: column; align-items: center; justify-content: center; gap: 8px;
  }
  .card-front .brand-mark { width: 14px; height: 14px; }
  .card-front .brand-name { font-size: 26px; }
  .card-front .divider { position: absolute; left: 150px; top: 20px; bottom: 30px; width: 1px; background: #d6d6d6; }
  .card-front .details { position: absolute; left: 162px; top: 22px; }
  .card-front .person { font-size: 9px; color: var(--green); font-weight: 500; }
  .card-front .role { font-size: 6px; color: var(--ink-soft); margin-bottom: 8px; }
  .card-front .footer-bar { height: 5px; bottom: 14px; }

  /* Business card back, white */
  .card-back { left: 830px; top: 350px; }
  .card-back .panel { position: absolute; right: 20px; top: 20px; width: 120px; height: 110px; background: var(--green); }
  .card-back .web { position: absolute; right: 18px; bottom: 14px; font-size: 7px; color: var(--ink); }

  /* Business card, green */
  .card-green { left: 560px; top: 580px; background: var(--green); }
  .card-green .panel { position: absolute; left: 30px; top: 20px; width: 110px; height: 110px; background: var(--green-dark); }
  .card-green .web { position: absolute; right: 18px; bottom: 14px; font-size: 7px; color: #fff; }
</style>
</head>
<body>

  <section class="sheet letterhead" aria-label="Letterhead">
    <div class="brand"><span class="brand-mark"></span><span class="brand-name">quorbanil</span></div>
    <div class="contact">
      <p>47 marbury close, fenwick</p>
      <p>NSW 2012, Australia</p>
      <p>T +61 (2) 5550 0142</p>
      <p>F +61 (2) 5550 0143</p>
      <p>M +61 (4) 5550 0144</p>
      <p>E nprothick@quorbanil.example</p>
      <p class="web">www.quorbanil.example</p>
    </div>
    <div class="watermark"></div>
    <div class="footer-bar"><span class="rule"></span><span class="url">www.quorbanil.example</span></div>
  </section>

  <section class="sheet envelope" aria-label="Envelope front">
    <div class="brand"><span class="brand-mark"></span><span class="brand-name">quorbanil</span></div>
    <div class="contact">
      <p>47 marbury close, fenwick</p>
      <p>NSW 2012, Australia</p>
    </div>
    <div class="footer-bar"><span class="rule"></span><span class="url">www.quorbanil.example</span></div>
  </section>

  <section class="sheet envelope-back" aria-label="Envelope back">
    <svg width="190" height="200" viewBox="0 0 190 200">
      <polygon points="0,200 95,110 190,200" fill="#ececec" stroke="#dcdcdc"/>
      <polygon points="0,0 95,90 190,0" fill="#ffffff" stroke="#dcdcdc"/>
    </svg>
    <span class="brand-mark"></span>
  </section>

  <section class="sheet card card-front" aria-label="Business card front">
    <div class="identity">
      <div class="brand"><span class="brand-mark"></span><span class="brand-name">quorbanil</span></div>
    </div>
    <div class="divider"></div>
    <div class="details">
      <p class="person">Neville Prothick</p>
      <p class="role">Technical Consultant</p>
      <div class="contact">
        <p>47 marbury close, fenwick</p>
        <p>NSW 2012, Australia</p>
        <p>T +61 (2) 5550 0142</p>
        <p>F +61 (2) 5550 0143</p>
        <p>M +61 (4) 5550 0144</p>
        <p>E nprothick@quorbanil.example</p>
      </div>
    </div>
    <div class="footer-bar"><span class="rule"></span><span class="url">www.quorbanil.example</span></div>
  </section>

  <section class="sheet card card-back" aria-label="Business card back">
    <div class="panel"></div>
    <p class="web">www.quorbanil.example</p>
  </section>

  <section class="sheet card card-green" aria-label="Business card, green version">
    <div class="panel"></div>
    <p class="web">www.quorbanil.example</p>
  </section>

</body>
</html>
```